Cloud Phone Service Brochure

We need a brochure for a Cloud Phone Service offering that we offer in Canada. We're a small company that cares about our client's success and protects their privacy. We would like to see designs that reflect us as a stable, trustworthy company which is also fast moving and leading edge. We see ourselves more like Quenby than Harn. Mosaic Vault has built our logo and business card, and we look forward to moving ahead here. I've attached our Business Card file so you have our logo as well as my own shot at some thoughts about content written as a trifold. That specific content does not need to be used, nor does it need to be a trifold. Those phone pictures are the actual phones we use.

```html
<!DOCTYPE html>
<html lang="en">
<head>
<meta charset="utf-8">
<title>Brightwire Signal – Cloud Phone Service Brochure</title>
<link rel="stylesheet" href="https://fonts.googleapis.com/css2?family=Montserrat:wght@400;500;600;700&display=swap">
<style>
  :root{
    --canvas:#e9e9ea;
    --blue:#2aa5df;
    --blue-deep:#1a86c2;
    --slate:#4a5058;
    --slate-dark:#3a3f46;
    --page-grey:#5f666e;
    --ink:#3c4148;
    --muted:#8a9099;
    --white:#ffffff;
    --sun-a:#f6a53a;
    --sun-b:#e8707a;
    --sun-c:#8c6bb3;
  }
  *{box-sizing:border-box;margin:0;padding:0}
  html,body{width:1200px;height:2440px;overflow:hidden}
  body{background:var(--canvas);font-family:"Montserrat",Arial,sans-serif;color:var(--ink);position:relative}

  .stage{position:absolute;left:0;width:1200px}
  .stage--cover{top:0;height:800px}
  .stage--outside{top:800px;height:820px}
  .stage--inside{top:1620px;height:820px}

  .page{position:absolute;width:400px;height:560px;overflow:hidden;box-shadow:0 10px 30px rgba(0,0,0,.18)}
  .page svg.page-art{position:absolute;inset:0;width:100%;height:100%}

  .stage--cover .page{left:400px;top:100px;transform:scale(1.1);transform-origin:top center}
  .page--left{left:200px;top:130px}
  .page--right{left:600px;top:130px}

  /* brand */
  .brand{position:absolute;display:flex;flex-direction:column;align-items:center;color:var(--white)}
  .brand__row{display:flex;align-items:center;gap:10px}
  .brand__mark{width:22px;height:22px;background:var(--white)}
  .brand__name{font-weight:600;font-size:17px;letter-spacing:2px;text-transform:uppercase}
  .brand__tag{font-size:7px;letter-spacing:3px;margin-top:6px;opacity:.9}
  .cover .brand{left:0;right:0;top:395px}

  /* back cover */
  .back{background:var(--white)}
  .back .brand{left:24px;top:22px;align-items:flex-start;color:var(--blue)}
  .back .brand__mark{background:var(--blue);width:16px;height:16px}
  .back .brand__name{font-size:11px;letter-spacing:1.5px}
  .back__intro{position:absolute;left:24px;top:62px;width:200px;font-size:8px;line-height:1.6;color:var(--ink)}
  .back__intro strong{display:block;font-size:9px;color:var(--slate-dark)}
  .back__scene{position:absolute;left:160px;top:120px;width:210px;height:96px}
  .back__partners-title{position:absolute;left:24px;top:238px;font-size:10px;font-weight:700;color:var(--blue)}
  .partners{position:absolute;left:24px;top:262px;width:352px;display:grid;grid-template-columns:repeat(4,1fr);gap:12px 14px}
  .partners span{height:22px;background:#d7dade;border-radius:3px}
  .back__line{position:absolute;left:24px;top:340px;font-size:8px;color:var(--muted)}
  .contact{position:absolute;left:0;right:0;top:460px;text-align:center;color:var(--white);font-size:8px;line-height:1.9}
  .contact b{font-weight:600}

  /* inside pages */
  .inside{background:var(--page-grey);color:#eef1f4}
  .inside h2{position:absolute;font-size:13px;font-weight:700;color:var(--white)}
  .inside p{position:absolute;font-size:8px;line-height:1.6;color:#d9dde2}
  .feature-list{position:absolute;list-style:none;font-size:8px;line-height:2.1;color:#e6e9ec}
  .feature-list li::before{content:"";display:inline-block;width:5px;height:5px;background:var(--blue);margin-right:7px;vertical-align:middle}
  .feature-list h3{font-size:9px;font-weight:700;color:var(--blue);margin-bottom:4px}
  .inside--left h2{left:30px;top:62px}
  .inside--left p{left:30px;top:86px;width:320px}
  .list--features{left:30px;top:130px}
  .list--plans{left:200px;top:118px}
  .inside--right h2{left:30px;top:190px}
  .list--why{left:30px;top:215px}
  .inside__sky{position:absolute;left:0;top:0;width:400px;height:170px}
  .inside__cables{position:absolute;left:200px;top:220px;width:170px;height:150px}
</style>
</head>
<body>

<!-- Front cover -->
<section class="stage stage--cover">
  <article class="page cover">
    <svg class="page-art" viewBox="0 0 400 560" preserveAspectRatio="none">
      <defs>
        <linearGradient id="sunset" x1="0" y1="0" x2="1" y2="1">
          <stop offset="0" stop-color="var(--sun-c)"/>
          <stop offset=".45" stop-color="var(--sun-b)"/>
          <stop offset="1" stop-color="var(--sun-a)"/>
        </linearGradient>
      </defs>
      <rect width="400" height="560" fill="#fff"/>
      <g role="img" aria-label="City skyline at sunset">
        <path d="M0 30 L240 0 Q330 60 400 70 L400 250 Q200 360 0 300Z" fill="url(#sunset)"/>
      </g>
      <path d="M200 0 L400 0 L400 70 Q330 60 240 0Z" fill="var(--slate)"/>
      <path d="M0 300 Q200 360 400 250 L400 560 L0 560Z" fill="var(--blue)"/>
      <path d="M0 300 Q200 360 400 250" fill="none" stroke="#fff" stroke-width="3"/>
    </svg>
    <div class="brand">
      <div class="brand__row"><span class="brand__mark"></span><span class="brand__name">Brightwire Signal</span></div>
      <span class="brand__tag">CLOUD PHONE SERVICES</span>
    </div>
  </article>
</section>

<!-- Outside spread: back + front -->
<section class="stage stage--outside">
  <article class="page page--left back">
    <svg class="page-art" viewBox="0 0 400 560" preserveAspectRatio="none">
      <rect width="400" height="560" fill="#fff"/>
      <path d="M0 410 Q200 370 400 430 L400 560 L0 560Z" fill="var(--blue)"/>
      <path d="M0 410 Q200 370 400 430" fill="none" stroke="var(--slate)" stroke-width="3"/>
    </svg>
    <div class="brand">
      <div class="brand__row"><span class="brand__mark"></span><span class="brand__name">Brightwire Signal</span></div>
    </div>
    <div class="back__intro">
      <strong>Cloud phone systems built for Canadian teams.</strong>
      Private, secure and always on.
    </div>
    <svg class="back__scene" viewBox="0 0 210 96" preserveAspectRatio="none" role="img" aria-label="Green landscape under a blue sky">
      <defs>
        <linearGradient id="meadow" x1="0" y1="0" x2="0" y2="1">
          <stop offset="0" stop-color="#6fb7e6"/>
          <stop offset=".55" stop-color="#a9d6ef"/>
          <stop offset=".6" stop-color="#7fbf5a"/>
          <stop offset="1" stop-color="#4f9a3c"/>
        </linearGradient>
      </defs>
      <rect width="210" height="96" fill="url(#meadow)"/>
    </svg>
    <div class="back__partners-title">Trusted Partners</div>
    <div class="partners">
      <span></span><span></span><span></span><span></span>
      <span></span><span></span><span></span><span></span>
    </div>
    <div class="back__line">Fast setup. Local support. No lock-in.</div>
    <div class="contact">
      <b>Call 1-800-555-0142</b><br>
      hello@brightwire.example<br>
      brightwire.example<br>
      Toronto, Ontario
    </div>
  </article>

  <article class="page page--right cover">
    <svg class="page-art" viewBox="0 0 400 560" preserveAspectRatio="none">
      <rect width="400" height="560" fill="#fff"/>
      <g role="img" aria-label="City skyline at sunset">
        <path d="M0 30 L240 0 Q330 60 400 70 L400 250 Q200 360 0 300Z" fill="url(#sunset)"/>
      </g>
      <path d="M200 0 L400 0 L400 70 Q330 60 240 0Z" fill="var(--slate)"/>
      <path d="M0 300 Q200 360 400 250 L400 560 L0 560Z" fill="var(--blue)"/>
      <path d="M0 300 Q200 360 400 250" fill="none" stroke="#fff" stroke-width="3"/>
    </svg>
    <div class="brand">
      <div class="brand__row"><span class="brand__mark"></span><span class="brand__name">Brightwire Signal</span></div>
      <span class="brand__tag">CLOUD PHONE SERVICES</span>
    </div>
  </article>
</section>

<!-- Inside spread -->
<section class="stage stage--inside">
  <article class="page page--left inside inside--left">
    <svg class="page-art" viewBox="0 0 400 560" preserveAspectRatio="none">
      <defs>
        <linearGradient id="greyPage" x1="0" y1="0" x2="1" y2="1">
          <stop offset="0" stop-color="#6b7279"/>
          <stop offset="1" stop-color="#50565d"/>
        </linearGradient>
      </defs>
      <rect width="400" height="560" fill="url(#greyPage)"/>
      <path d="M0 0 L170 0 Q90 25 0 50Z" fill="var(--blue)"/>
      <path d="M0 500 Q200 470 400 520 L400 560 L0 560Z" fill="var(--blue)"/>
    </svg>
    <h2>Business Phone Features</h2>
    <p>Everything your office needs, hosted in the cloud and managed for you.</p>
    <ul class="feature-list list--features">
      <li>Auto attendant</li>
      <li>Call forwarding</li>
      <li>Voicemail to email</li>
      <li>Conference bridge</li>
      <li>Mobile app</li>
      <li>Call recording</li>
    </ul>
    <ul class="feature-list list--plans">
      <h3>Plans</h3>
      <li>Starter line</li>
      <li>Business suite</li>
      <li>Enterprise</li>
      <li>Custom builds</li>
    </ul>
  </article>

  <article class="page page--right inside inside--right">
    <svg class="page-art" viewBox="0 0 400 560" preserveAspectRatio="none">
      <defs>
        <linearGradient id="greyPageR" x1="0" y1="0" x2="0" y2="1">
          <stop offset="0" stop-color="#3f454c"/>
          <stop offset="1" stop-color="#5c636a"/>
        </linearGradient>
      </defs>
      <rect width="400" height="560" fill="url(#greyPageR)"/>
      <path d="M260 560 Q340 520 400 470 L400 560Z" fill="var(--blue)"/>
    </svg>
    <svg class="inside__sky" viewBox="0 0 400 170" preserveAspectRatio="none" role="img" aria-label="Night sky with a glowing network horizon">
      <defs>
        <radialGradient id="glow" cx=".5" cy=".9" r=".7">
          <stop offset="0" stop-color="#8fc8ec"/>
          <stop offset=".5" stop-color="#2c4d6d"/>
          <stop offset="1" stop-color="#1d2630"/>
        </radialGradient>
      </defs>
      <rect width="400" height="170" fill="url(#glow)"/>
    </svg>
    <h2>Why Choose Us</h2>
    <ul class="feature-list list--why">
      <li>Canadian data centres</li>
      <li>Privacy first</li>
      <li>99.9% uptime</li>
      <li>Same-day setup</li>
      <li>Real people on support</li>
      <li>Simple monthly pricing</li>
    </ul>
    <svg class="inside__cables" viewBox="0 0 170 150" preserveAspectRatio="none" role="img" aria-label="Close-up of copper network cables">
      <defs>
        <linearGradient id="copper" x1="0" y1="0" x2="1" y2="1">
          <stop offset="0" stop-color="#7a4a32"/>
          <stop offset=".5" stop-color="#c07a4e"/>
          <stop offset="1" stop-color="#5a3626"/>
        </linearGradient>
      </defs>
      <rect width="170" height="150" fill="url(#copper)"/>
    </svg>
  </article>
</section>

</body>
</html>
```